Sydney law firm, Pelbury Solicitors, needs a flyer design!

We need a flyer design for our law firm which has been operating in Sydney for over 35 years. We want to send the flyer out to potential clients and also to existing clients to let them know the range of services that we provide. Our corporate colours are white, red and black and we would like these incorporated somewhat. The final design should be clean, modern and professional.

We would like the design to fit a double sided flyer approx. 210mm high x 100mm wide.

Law Firm

Serif
Sans Serif

eb2026
ffffff

• Details needed on the flyer are:
• Pelbury Solicitors
• 3/82 Tarrow Street, Liverpool, NSW 2170
• (02) 9413 5862
• www.pelburysolicitors-example.com.au
• info@pelburysolicitors-example.com.au
• Our areas of practice include:
• Property Law
• Conveyancing
• Leases
• Criminal Law
• Family Law
• Litigation and Dispute Resolution
• Company Law
• Wills and Estates
• Powers of Attorney and Guardianship
• a picture of scales or a picture of a gavel

```html
<!DOCTYPE html>
<html lang="en">
<head>
<meta charset="utf-8">
<title>Pelbury Solicitors – Flyer</title>
<link href="https://fonts.googleapis.com/css2?family=Roboto:wght@300;400;500;700&display=swap" rel="stylesheet">
<style>
  :root {
    --red: #c9352e;
    --band-red: #c4443c;
    --ink: #222222;
    --text: #444444;
    --rule: #c8c8c8;
    --footer: #d5d5d6;
    --page: #ffffff;
    --edge: #e2e2e2;
  }
  * { margin: 0; padding: 0; box-sizing: border-box; }
  html, body { width: 1200px; height: 824px; overflow: hidden; background: #ffffff; }
  body { position: relative; font-family: "Roboto", Arial, sans-serif; color: var(--text); }

  /* 100mm x 210mm panels */
  .page {
    position: absolute; top: 18px; width: 375px; height: 788px;
    background: var(--page); border-left: 1px solid var(--edge); border-right: 1px solid var(--edge);
  }
  .page--front { left: 195px; }
  .page--back { left: 630px; }
  .page__top-bar { position: absolute; top: 0; left: -1px; right: -1px; height: 7px; background: var(--red); }
  .page__bottom-bar { position: absolute; bottom: 0; left: -1px; right: -1px; height: 8px; background: var(--red); }

  .brand {
    position: absolute; top: 44px; left: 0; right: 0; text-align: center;
    color: var(--ink); font-weight: 400; text-transform: uppercase;
  }
  .brand__name { font-size: 36px; letter-spacing: 0.06em; line-height: 1; }
  .brand__sub { margin-top: 12px; font-size: 13px; letter-spacing: 0.6em; line-height: 1; padding-left: 0.6em; }

  .hero-rule { position: absolute; top: 122px; left: -1px; right: -1px; height: 4px; background: var(--red); }
  .hero-photo {
    position: absolute; top: 126px; left: -1px; right: -1px; height: 292px;
    background: radial-gradient(ellipse at 35% 55%, #8a8a8a 0%, #5a5a5a 40%, #2f2f2f 75%, #3d3d3d 100%);
  }
  .tagline {
    position: absolute; top: 418px; left: -1px; right: -1px; height: 78px;
    background: var(--band-red); color: #ffffff; text-align: center;
    font-weight: 300; font-size: 14.5px; line-height: 22px; padding-top: 17px;
  }
  .tagline strong { font-weight: 500; }

  .intro { position: absolute; top: 520px; left: 24px; right: 24px; font-size: 11px; line-height: 16px; color: var(--text); }
  .intro p + p { margin-top: 14px; font-weight: 700; color: #333; }

  .contact {
    position: absolute; top: 692px; left: -1px; right: -1px; height: 88px; background: var(--footer);
    font-size: 10px; line-height: 13px; color: #333;
  }
  .contact__name { position: absolute; left: 20px; top: 20px; color: var(--red); font-size: 13px; font-weight: 700; }
  .contact__address { position: absolute; left: 20px; top: 42px; }
  .contact__phone { position: absolute; right: 20px; top: 20px; color: var(--red); font-size: 13px; text-align: right; }
  .contact__phone strong { font-weight: 700; }
  .contact__web { position: absolute; right: 20px; top: 42px; text-align: right; }

  .practice__title {
    position: absolute; top: 42px; left: 0; right: 0; text-align: center;
    font-size: 24px; font-weight: 300; color: #333;
  }
  .practice__title strong { font-weight: 500; }
  .practice__title-rule { position: absolute; top: 78px; left: 24px; right: 24px; height: 3px; background: var(--red); }

  .practice__list { position: absolute; top: 108px; left: 14px; right: 14px; list-style: none; text-align: center; }
  .practice__item { padding-bottom: 8px; }
  .practice__item + .practice__item::before {
    content: ""; display: block; width: 160px; height: 1px; background: var(--rule); margin: 0 auto 8px;
  }
  .practice__heading { color: var(--red); font-size: 13.5px; font-weight: 500; line-height: 17px; }
  .practice__detail { font-size: 10px; line-height: 14px; color: var(--text); }
</style>
</head>
<body>

<section class="page page--front">
  <div class="page__top-bar"></div>
  <div class="brand">
    <div class="brand__name">Pelbury</div>
    <div class="brand__sub">Solicitors</div>
  </div>
  <div class="hero-rule"></div>
  <div class="hero-photo" role="img" aria-label="Black and white photograph of a man in a suit extending his hand for a handshake"></div>
  <div class="tagline">
    ESTABLISHED FOR <strong>OVER 35 YEARS</strong>,<br>
    YOU CAN <strong>FEEL CONFIDENT</strong> WITH OUR TEAM
  </div>
  <div class="intro">
    <p>Pelbury Solicitors is a private law firm based in Liverpool that has been servicing the Sydney area for over 35 years. With a dedicated, professional and friendly team we pride ourselves on delivering an exceptional legal service to our clients.</p>
    <p>Offering a complete legal service at affordable rates, our clients really do come first.</p>
  </div>
  <footer class="contact">
    <div class="contact__name">Pelbury Solicitors</div>
    <div class="contact__address">3/82 Tarrow Street,<br>Liverpool, NSW 2170</div>
    <div class="contact__phone">Phone: <strong>(02) 9413 5862</strong></div>
    <div class="contact__web">www.pelburysolicitors-example.com.au<br>info@pelburysolicitors-example.com.au</div>
  </footer>
  <div class="page__bottom-bar"></div>
</section>

<section class="page page--back">
  <div class="page__top-bar"></div>
  <h1 class="practice__title">OUR <strong>AREAS OF PRACTICE</strong></h1>
  <div class="practice__title-rule"></div>
  <ul class="practice__list">
    <li class="practice__item">
      <h2 class="practice__heading">PROPERTY LAW</h2>
      <p class="practice__detail">Advice, Residential and Commercial Property, Construction Contracts, Property Development, Building Disputes, Environmental Planning.</p>
    </li>
    <li class="practice__item">
      <h2 class="practice__heading">CONVEYANCING</h2>
      <p class="practice__detail">Advice, Buying and Selling Property, Contract Negotiations.</p>
    </li>
    <li class="practice__item">
      <h2 class="practice__heading">LEASES</h2>
      <p class="practice__detail">Advice, Commercial and Retail Leases, Industrial Leases, Lease negotiations, Surrender and Assignments of Lease.</p>
    </li>
    <li class="practice__item">
      <h2 class="practice__heading">CRIMINAL LAW</h2>
      <p class="practice__detail">Advice, Court Appearances, Pleas, Settlements, Trials, Bail Applications, Driving Offences, Drug Offences, Indictable Offences</p>
    </li>
    <li class="practice__item">
      <h2 class="practice__heading">FAMILY LAW</h2>
      <p class="practice__detail">Advice, Prenuptial Agreements, Divorce Applications, Settlements, Parenting Plans, Child Support, Mediation, Litigation.</p>
    </li>
    <li class="practice__item">
      <h2 class="practice__heading">LITIGATION AND DISPUTE</h2>
      <p class="practice__detail">Advice, Commercial Disputes, Civil Disputes, Construction Claims, Breach of Contract, Property and Lease Disputes, Dispute Resolution, Consumer Laws, Negligence, Litigation.</p>
    </li>
    <li class="practice__item">
      <h2 class="practice__heading">COMPANY LAW</h2>
      <p class="practice__detail">Advice, Buying and Selling Businesses, Structuring, Incorporation, Transactions, Shareholder Agreements, Confidentiality, Company Acquisitions, IP, PPS, Franchising.</p>
    </li>
    <li class="practice__item">
      <h2 class="practice__heading">WILLS AND ESTATES</h2>
      <p class="practice__detail">Advice, Will Interpretation, Estate Administration, Disputes, Probate, Letters of Administration.</p>
    </li>
    <li class="practice__item">
      <h2 class="practice__heading">POWERS OF ATTORNEY AND GUARDIANSHIP</h2>
      <p class="practice__detail">Advice, Drafting Powers of Attorney, Drafting Enduring Guardianship</p>
    </li>
  </ul>
  <footer class="contact">
    <div class="contact__name">Pelbury Solicitors</div>
    <div class="contact__address">3/82 Tarrow Street,<br>Liverpool, NSW 2170</div>
    <div class="contact__phone">Phone: <strong>(02) 9413 5862</strong></div>
    <div class="contact__web">www.pelburysolicitors-example.com.au<br>info@pelburysolicitors-example.com.au</div>
  </footer>
  <div class="page__bottom-bar"></div>
</section>

</body>
</html>
```